Toward Bright Morrow (TWBM) Business Card - company with a mission

Note* The file attached... orange with "Toward Bright MORROW" (in CAPS) is our logo. I am also open to having the text "toward bright morrow" OUTSIDE the orange round logo for business card (so yes, you may take the text out).

The info: (the following info are separate. So either you can use Martin or Helena for now, but that will be 2 separate cards, not together in one card. Thanks!!

Martin K Pardo
202.555.0183
martin@towardbrightmorrow.example
Managing Partner

Helena R Voss
202.555.0147
helena@towardbrightmorrow.example
Managing Partner

Our website: www.towardbrightmorrow.example

TWBM LLC stands for Toward Bright Morrow (non profit arm is called dawn lift foundation)—our business is based out of New York City and has a non-profit arm where for every bar of soap you purchase, we donate a bar (don’t want any designs that limits us to only soap). Currently working with South Africa. We want the focus to be organic/natural soap with a mission.

Looking for a clean, fresh design.

Industry/Entity Type

Non-Profit

Requirements
Must have
• Clean, fresh, refreshing. Design should not be too busy.

```html
<!DOCTYPE html>
<html lang="en">
<head>
<meta charset="utf-8">
<title>Toward Bright Morrow — Business Card</title>
<link rel="stylesheet" href="https://fonts.googleapis.com/css2?family=Inter:wght@300;400&display=swap">
<style>
  :root {
    --backdrop: #6b6c70;
    --card-orange: #f4ad64;
    --ink: #3b3e48;
    --white: #ffffff;
    --shadow: rgba(120, 70, 20, 0.35);
  }
  html, body {
    margin: 0;
    padding: 0;
    width: 1200px;
    height: 1200px;
    overflow: hidden;
    background: var(--backdrop);
  }
  .stage {
    position: relative;
    width: 1200px;
    height: 1200px;
    font-family: "Inter", Helvetica, Arial, sans-serif;
  }
  .card {
    position: absolute;
    left: 347px;
    top: 203px;
    width: 507px;
    height: 887px;
    background: var(--card-orange);
  }
  .brand-tab {
    position: absolute;
    left: 447px;
    top: 153px;
    width: 284px;
    height: 284px;
    border-radius: 50%;
    background: var(--card-orange);
    box-shadow: 0 10px 18px var(--shadow);
    display: flex;
    flex-direction: column;
    align-items: center;
    justify-content: center;
    color: var(--white);
    font-weight: 400;
    text-align: center;
    line-height: 1.1;
  }
  .brand-name-small {
    font-size: 22px;
    letter-spacing: 0.04em;
  }
  .brand-name-large {
    font-size: 40px;
    letter-spacing: 0.04em;
    margin-top: 4px;
  }
  .brand-dot {
    width: 16px;
    height: 16px;
    border-radius: 50%;
    background: var(--white);
    margin-bottom: 14px;
  }
  .contact {
    position: absolute;
    left: 75px;
    top: 472px;
    color: var(--ink);
    font-weight: 300;
  }
  .contact-name {
    font-size: 33px;
    font-weight: 400;
    margin: 0 0 10px;
  }
  .contact-line {
    font-size: 24px;
    margin: 0 0 6px;
  }
  .website {
    position: absolute;
    left: 0;
    right: 0;
    top: 798px;
    text-align: center;
    color: var(--white);
    font-size: 27px;
    font-weight: 300;
  }
</style>
</head>
<body>
  <div class="stage">
    <div class="card">
      <div class="contact">
        <p class="contact-name">Martin K Pardo</p>
        <p class="contact-line">202.555.0183</p>
        <p class="contact-line">martin@towardbrightmorrow.example</p>
        <p class="contact-line">Managing Partner</p>
      </div>
      <div class="website">www.towardbrightmorrow.example</div>
    </div>
    <div class="brand-tab">
      <div class="brand-dot"></div>
      <div class="brand-name-small">Toward Bright</div>
      <div class="brand-name-large">MORROW</div>
    </div>
  </div>
</body>
</html>
```